ashby paving works

Needs to have phone number 0412885107 and email marklowry@pavemail.com.au.
ABN 27613048852
name mark lowry

For all your concreting solutions
Excavation
Exposed & colour concrete
House & shed slabs
Driveways
Landing & steps

Contact Information for Business Card

ph 0412885107
email marklowry@pavemail.com.au.
ABN 27613048852
name mark lowry

```html
<!DOCTYPE html>
<html lang="en">
<head>
<meta charset="utf-8">
<title>Ashby Paving Works – Business Card</title>
<link href="https://fonts.googleapis.com/css2?family=Montserrat:wght@400;500;600;700&display=swap" rel="stylesheet">
<style>
  :root {
    --orange: #f26b21;
    --charcoal: #636162;
    --white: #ffffff;
    --backdrop: #d9d9d9;
    --ink-soft: #ececec;
  }
  * { box-sizing: border-box; margin: 0; padding: 0; }
  html, body { width: 1200px; height: 900px; overflow: hidden; }
  body {
    background: var(--backdrop);
    font-family: "Montserrat", sans-serif;
    display: flex;
    align-items: center;
    justify-content: center;
    gap: 40px;
  }
  .card {
    position: relative;
    width: 540px;
    height: 309px;
    background: var(--white);
    overflow: hidden;
    box-shadow: 0 6px 18px rgba(0,0,0,0.12);
  }

  /* Front */
  .card-front .band {
    position: absolute;
    left: 0; right: 0; bottom: 0;
    height: 66%;
    background: var(--orange);
  }
  .card-front .brand-mark {
    position: absolute;
    left: 50%; top: 34%;
    width: 40px; height: 40px;
    background: var(--charcoal);
    transform: translate(-50%, -50%);
  }
  .card-front .brand {
    position: absolute;
    left: 0; right: 0; top: 52%;
    text-align: center;
    color: var(--white);
  }
  .card-front .brand-name {
    font-weight: 700;
    font-size: 30px;
    letter-spacing: 1px;
    text-transform: uppercase;
    line-height: 1;
  }
  .card-front .brand-sub {
    display: flex;
    align-items: center;
    justify-content: center;
    gap: 14px;
    margin-top: 6px;
    font-weight: 500;
    font-size: 15px;
    letter-spacing: 6px;
    text-transform: uppercase;
  }
  .card-front .brand-sub .rule {
    width: 70px; height: 1.5px; background: var(--white);
  }

  /* Back */
  .card-back .panel {
    position: absolute;
    inset: 0;
    background: var(--charcoal);
    clip-path: polygon(48% 0, 100% 0, 100% 100%, 52% 100%, 52% 62%, 40% 38%);
  }
  .card-back .brand-mark {
    position: absolute;
    left: 34%; top: 28%;
    width: 58px; height: 58px;
    background: var(--orange);
  }
  .card-back .owner {
    position: absolute;
    left: 22px; bottom: 26px;
    color: var(--orange);
    font-size: 15px;
    line-height: 1.25;
  }
  .card-back .owner-name { font-weight: 600; font-size: 17px; }
  .card-back .services {
    position: absolute;
    left: 60%; top: 22px;
    list-style: none;
    color: var(--ink-soft);
    font-size: 12px;
    line-height: 1.55;
  }
  .card-back .services li { display: flex; align-items: center; gap: 7px; }
  .card-back .services li.lead { margin-left: -8px; }
  .card-back .services li:not(.lead)::before {
    content: ""; width: 5px; height: 5px; background: var(--orange); flex: none;
  }
  .card-back .contact {
    position: absolute;
    left: 56%; bottom: 24px;
    color: var(--white);
    font-size: 13px;
    line-height: 1.7;
  }
  .card-back .contact-row { display: flex; align-items: center; gap: 8px; }
  .card-back .contact-row svg { width: 13px; height: 13px; flex: none; }
</style>
</head>
<body>

  <section class="card card-front" aria-label="Business card front">
    <div class="band"></div>
    <div class="brand-mark"></div>
    <div class="brand">
      <div class="brand-name">Ashby Paving</div>
      <div class="brand-sub"><span class="rule"></span>Works<span class="rule"></span></div>
    </div>
  </section>

  <section class="card card-back" aria-label="Business card back">
    <div class="panel"></div>
    <div class="brand-mark"></div>
    <div class="owner">
      <div class="owner-name">mark lowry</div>
      <div class="owner-abn">ABN 27613048852</div>
    </div>
    <ul class="services">
      <li class="lead">For all your concreting solutions</li>
      <li>Excavation</li>
      <li>Exposed &amp; colour concrete</li>
      <li>House &amp; shed slabs</li>
      <li>Driveways</li>
      <li>Landing &amp; steps</li>
    </ul>
    <div class="contact">
      <div class="contact-row">
        <svg viewBox="0 0 16 16" aria-hidden="true"><rect x="4" y="1" width="8" height="14" rx="1.5" fill="none" stroke="#fff" stroke-width="1.5"/><circle cx="8" cy="12.5" r="0.9" fill="#fff"/></svg>
        <span>0412885107</span>
      </div>
      <div class="contact-row">
        <svg viewBox="0 0 16 16" aria-hidden="true"><rect x="1" y="3" width="14" height="10" fill="none" stroke="#fff" stroke-width="1.5"/><path d="M1 3l7 6 7-6" fill="none" stroke="#fff" stroke-width="1.5"/></svg>
        <span>marklowry@pavemail.com.au</span>
      </div>
    </div>
  </section>

</body>
</html>
```